Newly established winery needs label for its bottles

The Corvelle-Marsan Winery, is a small family owned winery that has been producing wine for little over 3 years. We are now ready to officially start commercializing our products. To do so we are looking for a label for our wine bottles. We are looking for a creative design that will differentiate our bottles from the more conventional labels. We are looking for one label design with 3 color schemes so that we can have a standard look and feel for all three of our wines, while having some differentiation between them with the different color schemes. In summary we are looking for a label that will standout by its uniqueness, simplicity and its modern touch. The label should also reflect the historical significance of the name of the winery. The attached documents offers more detail about the winery, what we are looking for, as well as some technical specification for the label. This label project is also related to a logo project see brief: http://www.pitchgallery.example/project-progress.aspx?briefId=553184). The logo project is now complete and the winning design source files were added to the documents in this brief. Also, details around the information that will need to appear on the label was added to the document list.
Updates
This label project will be on hold temporarily while the logo project is in progress. If you are interested in participating in the logo project, please follow this link: http://www.pitchgallery.example/project-progress.aspx?briefId=553184 Added Wednesday, December 17, 2014
Reason: Deadline extended to give sufficent time for submission and modification to the designs provided.

```html
<!DOCTYPE html>
<html lang="en">
<head>
<meta charset="utf-8">
<title>Corvelle-Marsan Winery – Wine Labels</title>
<link rel="stylesheet" href="https://fonts.googleapis.com/css2?family=Cinzel:wght@600&family=Archivo:wght@500;800&display=swap">
<style>
  :root {
    --bg: #ecebea;
    --ink: #141210;
    --emboss: rgba(60, 35, 15, .45);
    --emboss-soft: rgba(60, 35, 15, .25);
    --rose-light: #d99a52;
    --rose-base: #cc8438;
    --rose-deep: #b86a2c;
    --white-light: #d8ccab;
    --white-base: #c9b995;
    --white-deep: #b5a27c;
    --red-light: #b8682a;
    --red-base: #a3541e;
    --red-deep: #86421a;
  }
  * { box-sizing: border-box; margin: 0; padding: 0; }
  html, body { width: 1198px; height: 1200px; overflow: hidden; }
  body {
    background: var(--bg);
    display: flex;
    align-items: center;
    justify-content: center;
    gap: 40px;
  }
  .label {
    position: relative;
    width: 350px;
    height: 480px;
    color: var(--ink);
    font-family: "Archivo", Arial, sans-serif;
    box-shadow: 0 6px 18px rgba(0, 0, 0, .25);
    overflow: hidden;
  }
  .label__texture {
    position: absolute;
    inset: 0;
  }
  .label--rose .label__texture {
    background: linear-gradient(155deg, var(--rose-light), var(--rose-base) 50%, var(--rose-deep));
  }
  .label--white .label__texture {
    background: linear-gradient(155deg, var(--white-light), var(--white-base) 50%, var(--white-deep));
  }
  .label--red .label__texture {
    background: linear-gradient(155deg, var(--red-light), var(--red-base) 50%, var(--red-deep));
  }
  .winery {
    position: absolute;
    top: 100px;
    left: 0; right: 0;
    text-align: center;
    font-family: "Cinzel", Georgia, serif;
    font-weight: 600;
    font-size: 36px;
    letter-spacing: 3px;
    line-height: 1;
    color: var(--emboss);
  }
  .winery__name { display: block; }
  .winery__row {
    display: flex;
    align-items: center;
    justify-content: space-between;
    margin: 14px 16px;
  }
  .winery__tag {
    width: 118px;
    border-top: 1px solid var(--emboss);
    border-bottom: 1px solid var(--emboss);
    padding: 4px 0;
    font-family: "Archivo", Arial, sans-serif;
    font-weight: 500;
    font-size: 11px;
    letter-spacing: 2px;
    line-height: 1.3;
    color: var(--emboss);
    text-align: left;
  }
  .winery__tag--right { text-align: right; }
  .winery__mark {
    width: 56px; height: 56px;
    border-radius: 50%;
    background: var(--emboss-soft);
  }
  .vintage {
    position: absolute;
    top: 346px; left: 0; right: 0;
    text-align: center;
    font-weight: 500;
    font-size: 24px;
  }
  .variety {
    position: absolute;
    top: 376px; left: 0; right: 0;
    text-align: center;
    font-weight: 800;
    font-size: 30px;
    letter-spacing: 1px;
  }
  .volume, .alcohol {
    position: absolute;
    bottom: 12px;
    font-size: 11px;
    font-weight: 500;
    letter-spacing: .5px;
  }
  .volume { left: 14px; }
  .alcohol { right: 14px; }
</style>
</head>
<body>
  <article class="label label--rose">
    <div class="label__texture" role="img" aria-label="Aged paper texture with soft diagonal colour washes in amber tones"></div>
    <h1 class="winery">
      <span class="winery__name">CORVELLE</span>
      <span class="winery__row">
        <span class="winery__tag">VIGNOBLE<br>FAMILIAL</span>
        <span class="winery__mark"></span>
        <span class="winery__tag winery__tag--right">FAMILY<br>WINERY</span>
      </span>
      <span class="winery__name">MARSAN</span>
    </h1>
    <p class="vintage">2014</p>
    <p class="variety">ROSÉ WINE</p>
    <p class="volume">750 ML.</p>
    <p class="alcohol">ALC. 12% BY VOLUME</p>
  </article>
  <article class="label label--white">
    <div class="label__texture" role="img" aria-label="Aged paper texture with soft diagonal colour washes in cream tones"></div>
    <h1 class="winery">
      <span class="winery__name">CORVELLE</span>
      <span class="winery__row">
        <span class="winery__tag">VIGNOBLE<br>FAMILIAL</span>
        <span class="winery__mark"></span>
        <span class="winery__tag winery__tag--right">FAMILY<br>WINERY</span>
      </span>
      <span class="winery__name">MARSAN</span>
    </h1>
    <p class="vintage">2014</p>
    <p class="variety">WHITE WINE</p>
    <p class="volume">750 ML.</p>
    <p class="alcohol">ALC. 12% BY VOLUME</p>
  </article>
  <article class="label label--red">
    <div class="label__texture" role="img" aria-label="Aged leather-like texture with soft diagonal colour washes in rust tones"></div>
    <h1 class="winery">
      <span class="winery__name">CORVELLE</span>
      <span class="winery__row">
        <span class="winery__tag">VIGNOBLE<br>FAMILIAL</span>
        <span class="winery__mark"></span>
        <span class="winery__tag winery__tag--right">FAMILY<br>WINERY</span>
      </span>
      <span class="winery__name">MARSAN</span>
    </h1>
    <p class="vintage">2014</p>
    <p class="variety">RED WINE</p>
    <p class="volume">750 ML.</p>
    <p class="alcohol">ALC. 12% BY VOLUME</p>
  </article>
</body>
</html>
```